Guarding One's Body Using Sharp Steel Cover

Hi we are producing a self defense course entitled Guarding One's Body Using Sharp Steel: A Complete Manual For Learning The Finest And Handiest Wilderness Tool In Recorded History.

I listed this as a book cover but it will actually be a DVD set, but the book cover model works fine.

See below for design examples - I am thinking we need a cover that will appeal to military/survival type people.

Target Market(s)

survivalists, cops, preppers, gun owners, martial artists, and average people wanting to learn how to defend themselves

Industry/Entity Type

Defense

Requirements
Must have
• Title: GUARDING ONE'S BODY USING SHARP STEEL: A COMPLETE MANUAL FOR LEARNING THE FINEST AND HANDIEST WILDERNESS TOOL IN RECORDED HISTORY
Nice to have
• Please look at these sample designs from other books as a model:
• https://files.plorvexa.org/media/en/4/27/BrindelQXMP.jpg - This stye is ideal.
• Other good examples:
• https://pics2.talvorn.com/8143907_k370.jpg
• http://m.zephquill.com/titles/2719058463k/48071935.jpg
• http://img.crondelmart.com/pics/P/73Tm58QyzFr._BX_KL410_TR316,410_.jpg
• http://3.cdn.wendoplix.net/-RTyZWLMMKAQ/BNWq_hufxaT/BBBBBBBBv8G/DKNp815ZaXW/s1600/Q4710392.JPG

```html
<!DOCTYPE html>
<html lang="en">
<head>
<meta charset="utf-8">
<title>Guarding One's Body Using Sharp Steel — Cover</title>
<link rel="stylesheet" href="https://fonts.googleapis.com/css2?family=Alfa+Slab+One&family=Black+Ops+One&family=Graduate&family=Montserrat:wght@500&display=swap">
<style>
  :root{
    --backdrop:#2f4f52;
    --wood-dark:#2a1c12;
    --wood-mid:#3e2a1b;
    --wood-light:#4d3422;
    --author-grey:#9c9a96;
    --label-tan:#bdb3a7;
    --title-yellow:#e9ec2a;
    --title-green:#4fb531;
    --title-edge:#1f3d12;
    --sub-white:#dcdcd8;
    --blade-steel:#566e71;
    --handle-steel:#3f5658;
  }
  *{margin:0;padding:0;box-sizing:border-box}
  html,body{width:1200px;height:1000px;overflow:hidden}
  body{
    background:radial-gradient(ellipse at 55% 45%, #3a6163 0%, var(--backdrop) 70%);
    position:relative;
  }
  .cover{
    position:absolute;left:280px;top:30px;width:640px;height:940px;
    background:
      radial-gradient(ellipse at 40% 35%, var(--wood-light) 0%, transparent 60%),
      linear-gradient(180deg, var(--wood-mid) 0%, var(--wood-dark) 100%);
    box-shadow:0 18px 40px rgba(0,0,0,.45);
    overflow:hidden;
    text-align:center;
  }
  .cover > *{position:absolute;left:0;right:0}
  .author{
    top:70px;font:34px/1 "Graduate",serif;letter-spacing:5px;color:var(--author-grey);
  }
  .imprint{
    top:128px;font:500 9px/1 "Montserrat",sans-serif;letter-spacing:3px;color:var(--label-tan);
  }
  .title-lead,.title-key{
    font-family:"Black Ops One",sans-serif;
    background:linear-gradient(180deg,var(--title-yellow) 0%,var(--title-green) 100%);
    -webkit-background-clip:text;background-clip:text;color:transparent;
    -webkit-text-stroke:1.5px var(--title-edge);
  }
  .title-lead{font-size:34px;line-height:1;letter-spacing:1px}
  .title-lead.line-one{top:190px}
  .title-lead.line-two{top:232px}
  .title-key{
    top:280px;font-size:156px;line-height:1;letter-spacing:4px;
    -webkit-text-stroke:4px var(--title-edge);
    filter:drop-shadow(5px 5px 0 #1a120b);
  }
  .knife-art{left:70px;right:auto;width:500px;height:80px}
  .knife-art.upper{top:478px}
  .knife-art.lower{top:800px;height:96px}
  .subtitle-main{
    font:40px/1 "Alfa Slab One",serif;color:var(--sub-white);letter-spacing:1px;
  }
  .subtitle-small{
    font:13px/1 "Alfa Slab One",serif;color:var(--sub-white);letter-spacing:1px;
  }
  .subtitle-main.line-a{top:590px}
  .subtitle-small.line-b{top:636px}
  .subtitle-main.line-c{top:658px}
  .subtitle-small.line-d{top:704px}
</style>
</head>
<body>
  <main class="cover">
    <p class="author">DALTON R. WHITFIELD</p>
    <p class="imprint">IRONHOLD FIELD VIDEO</p>

    <h1 class="title">
      <span class="title-lead line-one" style="position:absolute;left:0;right:0">GUARDING ONE'S BODY</span>
      <span class="title-lead line-two" style="position:absolute;left:0;right:0">USING SHARP</span>
      <span class="title-key" style="position:absolute;left:0;right:0">STEEL</span>
    </h1>

    <svg class="knife-art upper" viewBox="0 0 500 80" role="img" aria-label="Illustration of a combat knife pointing left">
      <rect x="0" y="18" width="290" height="44" rx="22" fill="var(--blade-steel)"/>
      <rect x="290" y="8" width="210" height="64" rx="20" fill="var(--handle-steel)"/>
    </svg>

    <h2 class="subtitle">
      <span class="subtitle-main line-a" style="position:absolute;left:0;right:0">A COMPLETE MANUAL</span>
      <span class="subtitle-small line-b" style="position:absolute;left:0;right:0">FOR LEARNING THE FINEST AND HANDIEST</span>
      <span class="subtitle-main line-c" style="position:absolute;left:0;right:0">WILDERNESS TOOL</span>
      <span class="subtitle-small line-d" style="position:absolute;left:0;right:0">IN RECORDED HISTORY.</span>
    </h2>

    <svg class="knife-art lower" viewBox="0 0 500 96" role="img" aria-label="Illustration of a combat knife pointing right">
      <rect x="0" y="14" width="230" height="68" rx="22" fill="var(--handle-steel)"/>
      <rect x="230" y="26" width="270" height="48" rx="24" fill="var(--blade-steel)"/>
    </svg>
  </main>
</body>
</html>
```